Website concept design - need very creative and polished web page layouts

Need 3-4 web pages designed (graphic only). Client is an interior designer and has specific design requirements. Need a skilled graphic designer to help me create a concept for the new site.

The site is primarily meant to allow users to build and buy a new product, but should have a portfolio site feel. I have specific requirements so designer won't have to 'figure it out' on their own.

Making use of white space, text orientation, and object movement are essential to the success of this project.

Inspirational sites:

http://brinmoss.example/#en - creative and atypical
https://quolvane.example/ - white space and movement; vertical menu links
https://784k.example- modern into, object hover movement
https://www.tembrosk.example/case-silver-harbor - white space, dimensional feel of objects floating on page; pop of color

Target Market(s)

Interior designers and individuals - both commercial and retail.

Industry/Entity Type

Interior Design

Number of Pages Required

4 page

Font styles to use
Serif
Sans Serif

Requirements
Must have
• Professional design, meet design requirements, professional and highly creative look. This cannot look like or resemble in any way a common or typical website. Making use of white space, text orientation, and object movement are essential to the success of this project.
• Colors for the project:
• COLOR TREATMENT - (Not Final)
• DARK PUTTY – 77% Black
• R 95
• G 96
• B 98
• LIGHT PUTTY – 50% Black
• R 129
• G 131
• B 134
• ** Other Levels of Putty can be used.
• BLUE GREEN - (May not be final)
• R 113
• G 202
• B 210
Should not have
• Cannot look like or resemble a typical website design.

```html
<!DOCTYPE html>
<html lang="en">
<head>
<meta charset="utf-8">
<title>Vestra — Visualize Your Room Into A Masterpiece</title>
<link rel="stylesheet" href="https://fonts.googleapis.com/css2?family=Bodoni+Moda:ital,wght@0,400;0,500;1,400;1,500&family=Jost:wght@400;500&display=swap">
<style>
  :root {
    --page-white: #ffffff;
    --ink: #141414;
    --ink-soft: #3a3b3d;
    --putty-dark: #5f6062;
    --putty-light: #818386;
    --blue-green: #71cad2;
    --bar-black: #161616;
    --photo-light: #e9e1d3;
    --photo-mid: #cbb99c;
    --photo-deep: #5e5144;
  }
  * { margin: 0; padding: 0; box-sizing: border-box; }
  html, body {
    width: 1200px; height: 900px; overflow: hidden;
    background: var(--page-white);
    font-family: "Jost", sans-serif;
    color: var(--ink);
  }
  .hero { position: relative; width: 1200px; height: 900px; overflow: hidden; }

  .accent-rail {
    position: absolute; left: 14px; top: 0; width: 12px; height: 900px;
    background: var(--blue-green);
  }

  .brand {
    position: absolute; left: 52px; top: 52px;
    font-family: "Bodoni Moda", serif; font-weight: 500;
    font-size: 26px; letter-spacing: 1px; color: var(--ink);
  }
  .menu-toggle {
    position: absolute; left: 236px; top: 60px;
    display: flex; align-items: center; gap: 10px;
    font-size: 14px; color: var(--ink-soft);
  }
  .menu-toggle svg { display: block; }

  .hero-photo {
    position: absolute; left: 588px; top: 0; width: 612px; height: 900px;
    background:
      linear-gradient(180deg, rgba(255,255,255,0) 55%, rgba(70,60,52,0.55) 100%),
      linear-gradient(100deg, var(--photo-light) 0%, #ddd0bb 35%, var(--photo-mid) 65%, #b59d7c 100%);
  }
  .hero-photo::after {
    content: ""; position: absolute; left: 0; right: 0; bottom: 0; height: 260px;
    background: linear-gradient(180deg, rgba(94,81,68,0) 0%, var(--photo-deep) 100%);
    opacity: 0.6;
  }

  .utility-bar {
    position: absolute; right: 0; top: 0; width: 335px; height: 130px;
    background: var(--bar-black);
    display: flex; align-items: center; justify-content: space-around;
    padding: 0 28px;
  }
  .utility-bar .login {
    display: flex; align-items: center; gap: 9px;
    color: var(--blue-green); font-size: 16px;
  }

  .headline {
    position: absolute; left: 230px; top: 250px;
    font-family: "Bodoni Moda", serif; font-style: italic; font-weight: 500;
    font-size: 62px; line-height: 1.08; color: var(--ink);
    white-space: nowrap;
  }
  .tagline {
    position: absolute; left: 230px; top: 538px;
    font-size: 19px; font-weight: 500; color: var(--ink);
  }

  .discover-link {
    position: absolute; left: 230px; top: 748px;
    display: flex; align-items: center; gap: 8px;
    font-size: 15px; color: var(--ink-soft);
    padding-bottom: 4px; border-bottom: 1px solid var(--ink-soft);
  }

  .slide-controls {
    position: absolute; left: 520px; top: 738px; height: 48px;
    display: flex;
  }
  .slide-controls .prev,
  .slide-controls .next {
    width: 68px; height: 48px; display: flex; align-items: center; justify-content: center;
  }
  .slide-controls .prev { background: var(--page-white); border: 1.5px solid var(--ink); }
  .slide-controls .next { background: var(--bar-black); width: 72px; }

  .scroll-cue {
    position: absolute; left: 44px; top: 800px;
    display: flex; align-items: center; gap: 8px;
    transform: rotate(-90deg); transform-origin: left top;
    font-size: 12px; color: var(--ink-soft);
  }
</style>
</head>
<body>
<main class="hero">
  <div class="accent-rail"></div>

  <div class="brand">VESTRA</div>

  <div class="menu-toggle">
    <svg width="16" height="12" viewBox="0 0 16 12" aria-hidden="true">
      <rect x="0" y="0" width="16" height="1.6" fill="#71cad2"/>
      <rect x="0" y="5" width="16" height="1.6" fill="#71cad2"/>
      <rect x="0" y="10" width="16" height="1.6" fill="#71cad2"/>
    </svg>
    <span>Menu</span>
  </div>

  <div class="hero-photo" role="img" aria-label="Interior photograph: warm wooden dining corner with round table, woven chair, pendant lamps and wall shelves"></div>

  <nav class="utility-bar">
    <svg width="18" height="18" viewBox="0 0 18 18" aria-label="Search">
      <circle cx="7.5" cy="7.5" r="5.5" fill="none" stroke="#ffffff" stroke-width="2"/>
      <line x1="11.5" y1="11.5" x2="16" y2="16" stroke="#ffffff" stroke-width="2"/>
    </svg>
    <span class="login">
      <svg width="16" height="18" viewBox="0 0 16 18" aria-hidden="true">
        <circle cx="8" cy="5" r="4" fill="#71cad2"/>
        <path d="M0 18 C0 11 16 11 16 18 Z" fill="#71cad2"/>
      </svg>
      Login
    </span>
    <svg width="20" height="18" viewBox="0 0 20 18" aria-label="Cart">
      <path d="M1 2 H4 L6.5 12 H16 L18 5 H5" fill="none" stroke="#ffffff" stroke-width="1.8"/>
      <circle cx="8" cy="15.5" r="1.6" fill="#ffffff"/>
      <circle cx="15" cy="15.5" r="1.6" fill="#ffffff"/>
    </svg>
  </nav>

  <h1 class="headline">Visualize<br>Your Room Into<br>A Masterpiece!</h1>
  <p class="tagline">Great Product Quality with Outstanding Design</p>

  <a class="discover-link">Discover More
    <svg width="14" height="10" viewBox="0 0 14 10" aria-hidden="true">
      <path d="M0 5 H12 M8 1 L12 5 L8 9" fill="none" stroke="#3a3b3d" stroke-width="1.4"/>
    </svg>
  </a>

  <div class="slide-controls">
    <span class="prev">
      <svg width="20" height="10" viewBox="0 0 20 10" aria-label="Previous">
        <path d="M20 5 H2 M6 1 L2 5 L6 9" fill="none" stroke="#141414" stroke-width="1.6"/>
      </svg>
    </span>
    <span class="next">
      <svg width="20" height="10" viewBox="0 0 20 10" aria-label="Next">
        <path d="M0 5 H18 M14 1 L18 5 L14 9" fill="none" stroke="#ffffff" stroke-width="1.6"/>
      </svg>
    </span>
  </div>

  <div class="scroll-cue">
    <svg width="14" height="8" viewBox="0 0 14 8" aria-hidden="true">
      <path d="M14 4 H2 M5 1 L2 4 L5 7" fill="none" stroke="#3a3b3d" stroke-width="1.3"/>
    </svg>
    <span>Scroll</span>
  </div>
</main>
</body>
</html>
```